Quillbase Design Project - BrightPickDigest

Take a look at this website, gridvault.example. We are creating something very similar to this, four pages are required. The name of our website is BrightPickDigest.example
1) The home page which highlights, app of the day, a carousel which highlights featured apps, and top apps in different categories
2) Single App Page - This page will details the app that is selected, app icon, app description, app ratings, and other information you can find on an app page in the lumora market
3) A page that list all the apps in a category, for example if the user select, "100 top apps" the page that will display the list of 100 apps, 10 per page, summary of description, a small icon, screenshot etc for each app
4) Review Page - where we review an app of the day, including screenshots, videos, text reviews etc
I do not have any logo at the moment, use these as nav links; home, my apps, reviews, blog and contact. Thank you.
I will like to see a nice creativity. I am open to a very beautiful color combinations. Thank you
Target Market(s)
App shoppers, people that are looking for new apps, discounted apps etc
Industry/Entity Type
Store
Look and feel

```html
<!DOCTYPE html>
<html lang="en">
<head>
<meta charset="utf-8">
<title>BrightPickDigest</title>
<link rel="stylesheet" href="https://fonts.googleapis.com/css2?family=Open+Sans:wght@300;400;600;700&family=Source+Sans+3:wght@400;600;700&display=swap">
<style>
:root{
  --ink:#24273a;
  --ink-text:#2c2c2c;
  --blue:#1f5aa8;
  --blue-link:#2a6cc0;
  --sky:#3cb2de;
  --sky-light:#6fd0ef;
  --orange:#f39c12;
  --gold:#f6b31a;
  --grey-bg:#efefef;
  --grey-text:#666;
  --white:#fff;
}
*{box-sizing:border-box;margin:0;padding:0}
html,body{width:1167px;height:1200px;overflow:hidden}
body{font-family:"Open Sans",sans-serif;color:var(--ink-text);background:var(--white);position:relative}
.abs{position:absolute}

/* top bar */
.topbar{left:0;top:0;width:1167px;height:27px;background:var(--ink);font-size:10px}
.topbar .account{position:absolute;right:202px;top:8px;color:#5aa3e6;font-weight:600}
.topbar .points{position:absolute;right:134px;top:7px;color:var(--gold);font-size:11px;font-weight:600}

/* header */
.header{left:0;top:27px;width:1167px;height:92px;background:var(--white)}
.logo{position:absolute;left:165px;top:28px;font-size:29px;font-weight:400;color:var(--blue);white-space:nowrap}
.nav{position:absolute;left:473px;top:0;display:flex;height:92px}
.nav a{display:flex;align-items:center;justify-content:center;width:113px;height:92px;border-right:1px solid #ddd;color:#222;font-size:14px;text-decoration:none}
.nav a.active{background:var(--ink);color:#5fc2ee}

/* hero */
.hero{left:0;top:119px;width:1167px;height:359px;background:radial-gradient(ellipse at 60% 30%,#47c0e8,#36a9d6 70%)}
.aotd{position:absolute;left:151px;top:22px;width:314px;height:313px;border-radius:6px;overflow:hidden;box-shadow:0 2px 6px rgba(0,0,0,.25)}
.aotd .shot{height:259px;background:linear-gradient(180deg,#d9c9a2 0%,#b9a37f 40%,#6a6a72 75%,#4a4a52 100%)}
.aotd .label{height:54px;background:var(--ink);color:#fff;font-size:28px;font-weight:300;display:flex;align-items:center;justify-content:center}
.panel{position:absolute;top:30px;height:202px;background:rgba(255,255,255,.08);border-radius:4px}
.info{left:516px;width:230px;padding:16px 19px;font-family:"Source Sans 3",sans-serif;color:#fff}
.info h2{font-size:16px;font-weight:400;letter-spacing:-.3px}
.info .price{font-family:"Open Sans",sans-serif;font-weight:700;font-size:15px;color:#111;margin-top:2px}
.info .stars{display:flex;gap:4px;margin-top:3px}
.info .meta{font-size:12px;line-height:13px;margin-top:9px}
.info .thumbs{position:absolute;left:20px;top:140px;display:flex;align-items:center}
.thumb{width:36px;height:52px;background:linear-gradient(160deg,#a89a7c,#4c4a40);margin-right:20px}
.thumbs .arrow{margin-right:12px}
.desc{left:753px;width:228px;padding:18px 10px 18px 12px;color:#fff;font-size:11.6px;line-height:14px;letter-spacing:-.1px}
.desc hr{border:0;border-top:1px solid rgba(255,255,255,.3);margin:31px 0 22px}
.desc .last{padding-right:2px}
.dl-icon{position:absolute;right:17px;bottom:6px}
.btn{position:absolute;top:275px;height:35px;display:flex;align-items:center;font-size:14px;border-radius:2px}
.btn-download{left:514px;width:144px;background:linear-gradient(#fff,#e6e6e6);color:#222;padding-left:17px;gap:13px}
.btn-share{left:668px;width:148px;background:linear-gradient(#3d72c0,#2a57a0);color:#fff;padding-left:19px;gap:19px;font-weight:600}
.btn-tweet{left:825px;width:147px;background:linear-gradient(#8fe0f6,#6fd0ef);color:#fff;padding-left:22px;gap:20px;font-weight:600}
.sq{width:19px;height:19px;background:rgba(255,255,255,.85);border-radius:2px}
.btn-share .sq{background:#fff}

/* featured */
.featured{left:0;top:478px;width:1167px;height:314px;background:var(--grey-bg)}
.tabs{position:absolute;left:150px;top:19px;display:flex;gap:10px}
.tab{height:39px;display:flex;align-items:center;justify-content:center;color:#fff;font-size:15px;border-radius:3px 3px 0 0}
.tab.orange{width:100px;background:var(--orange)}
.tab.blue{width:100px;background:var(--blue)}
.tab.blue.wide{width:110px}
.more-link{position:absolute;font-size:12.5px;color:var(--blue-link);white-space:nowrap}
.more-link b{color:#222;margin-right:6px}
.carousel{position:absolute;left:150px;top:58px;width:866px;height:241px;background:#fff;border-top:3px solid var(--orange)}
.card{position:absolute;top:20px;width:177px}
.card .pic{height:132px}
.card h3{font-size:12.5px;font-weight:400;color:var(--blue);margin-top:11px}
.card p{font-size:10.5px;color:var(--grey-text);line-height:13px;margin-top:5px;width:150px}
.card .more{font-size:9.5px;color:var(--blue);margin-top:6px;display:flex;gap:13px}
.card .more span{color:var(--orange);font-weight:700}
.nav-circle{position:absolute;top:615px;width:66px;height:66px;border-radius:50%;background:var(--grey-bg);display:flex;align-items:center}

/* more apps */
.more-apps{left:170px;top:820px;width:846px}
.more-apps h2{font-size:15px;font-weight:600;color:#333;padding-left:1px;padding-bottom:8px;border-bottom:2px solid #ccc}
.app{position:absolute;width:100px;margin-left:-50px;text-align:center}
.app .price{font-weight:600;font-size:15px;color:var(--blue);line-height:18px}
.app .icon{width:68px;height:68px;border-radius:12px;margin:0 auto;box-shadow:0 1px 2px rgba(0,0,0,.35)}
.app .name{font-size:11px;color:#666;margin-top:6px}

/* footer */
.footer{left:0;top:1147px;width:1167px;height:53px;background:var(--ink);color:#fff;font-size:12.5px;display:flex;align-items:center;justify-content:center}
</style>
</head>
<body>

<div class="abs topbar"><span class="account">My Account:</span><span class="points">125 Points</span></div>

<header class="abs header">
  <div class="logo">BrightPickDigest</div>
  <nav class="nav">
    <a class="active" href="#">HOME</a><a href="#">MY APPS</a><a href="#">REVIEWS</a><a href="#">BLOG</a><a href="#">CONTACT</a>
  </nav>
</header>

<section class="abs hero">
  <div class="aotd">
    <div class="shot" role="img" aria-label="Racing game scene with two sports cars on a city street lined with blossom trees"></div>
    <div class="label">APP OF THE DAY</div>
  </div>

  <div class="panel info">
    <h2>Gravity Drift: Racing Cars</h2>
    <div class="price">FREE</div>
    <div class="stars">
      <svg width="108" height="24" viewBox="0 0 108 24"><g fill="#f6a41a"><path id="st" d="M12 1l3.2 7 7.6.8-5.7 5.1 1.6 7.5L12 17.6 5.3 21.4l1.6-7.5L1.2 8.8 8.8 8z"/><use href="#st" x="28"/><use href="#st" x="56"/><use href="#st" x="84"/></g></svg>
    </div>
    <div class="meta">Action / Cars<br>Developer: Brightcask Media</div>
    <div class="thumbs">
      <svg class="arrow" width="10" height="16" viewBox="0 0 10 16"><path d="M8 2L2 8l6 6" stroke="#fff" stroke-width="3" fill="none"/></svg>
      <div class="thumb" role="img" aria-label="Game screenshot"></div>
      <div class="thumb" role="img" aria-label="Game screenshot"></div>
      <div class="thumb" role="img" aria-label="Game screenshot" style="margin-right:12px"></div>
      <svg width="10" height="16" viewBox="0 0 10 16"><path d="M2 2l6 6-6 6" stroke="#fff" stroke-width="3" fill="none"/></svg>
    </div>
  </div>

  <div class="panel desc">
    <p>Gravity Drift will capative you with amazing gravity-twising.Charm-matching action across 40 unique levels!</p>
    <hr>
    <p class="last">Rotate your device in all 4 orientations to change the direction of gravity! play it once and you will be hooked!</p>
    <svg class="dl-icon" width="28" height="28" viewBox="0 0 28 28"><rect width="28" height="28" rx="4" fill="#f39c12"/><path d="M14 6v11M9 12l5 5 5-5M8 21h12" stroke="#fff" stroke-width="2.6" fill="none"/></svg>
  </div>

  <div class="btn btn-download">
    <svg width="20" height="20" viewBox="0 0 20 20"><circle cx="10" cy="10" r="9" fill="#f39c12"/><path d="M10 5v8M6.5 10l3.5 3.5 3.5-3.5" stroke="#fff" stroke-width="2" fill="none"/></svg>DOWNLOAD
  </div>
  <div class="btn btn-share"><span class="sq"></span>SHARE</div>
  <div class="btn btn-tweet"><span class="sq"></span>TWEET</div>
</section>

<section class="abs featured">
  <div class="tabs">
    <div class="tab orange">Featured</div>
    <div class="tab blue">Popular</div>
    <div class="tab blue wide">Top Rated</div>
  </div>
  <div class="more-link" style="left:862px;top:36px"><b>»</b>View More Applications</div>
  <div class="carousel">
    <div class="card" style="left:46px">
      <div class="pic" role="img" aria-label="Bowling ball striking white pins" style="background:linear-gradient(135deg,#8a8a8a,#e8e8e8 55%,#c83a3a)"></div>
      <h3>3D Bowling</h3><p>Lorem Ipsum Dolor Sit amet and type</p><div class="more">Click for more <span>»</span></div>
    </div>
    <div class="card" style="left:245px">
      <div class="pic" role="img" aria-label="Orange tuned sports car at night" style="background:linear-gradient(135deg,#0f1a2a,#2a3a58 45%,#e8821e 75%,#f0a040)"></div>
      <h3>Turbo Lane Rush</h3><p>Lorem Ipsum Dolor Sit amet and type</p><div class="more">Click for more <span>»</span></div>
    </div>
    <div class="card" style="left:443px">
      <div class="pic" role="img" aria-label="Red bicycle against a blue sky" style="background:linear-gradient(135deg,#1f6fc0,#5fb0ee 60%,#b83040)"></div>
      <h3>Pedal Dash</h3><p>Lorem Ipsum Dolor Sit amet and type</p><div class="more">Click for more <span>»</span></div>
    </div>
    <div class="card" style="left:642px">
      <div class="pic" role="img" aria-label="Soldier with rifle in a desert town" style="background:linear-gradient(160deg,#b9a079,#8b7455 55%,#3a3a36)"></div>
      <h3>Dune Patrol Strike</h3><p>Lorem Ipsum Dolor Sit amet and type</p><div class="more">Click for more <span>»</span></div>
    </div>
  </div>
</section>
<div class="nav-circle" style="left:131px;padding-left:24px"><svg width="14" height="20" viewBox="0 0 14 20"><path d="M11 2L3 10l8 8" stroke="#1f5aa8" stroke-width="4" fill="none"/></svg></div>
<div class="nav-circle" style="left:984px;padding-left:28px"><svg width="14" height="20" viewBox="0 0 14 20"><path d="M3 2l8 8-8 8" stroke="#1f5aa8" stroke-width="4" fill="none"/></svg></div>

<section class="abs more-apps">
  <h2>More Applications</h2>
  <div class="more-link" style="left:692px;top:2px"><b>»</b>View More Applications</div>
</section>

<div class="abs" style="left:0;top:0">
  <div class="app" style="left:204px;top:871px"><div class="price">FREE</div><div class="icon" role="img" aria-label="Zombies app icon" style="background:radial-gradient(#9ccf5a,#1d2a1a)"></div><div class="name">Zombies</div></div>
  <div class="app" style="left:333px;top:871px"><div class="price">FREE</div><div class="icon" role="img" aria-label="Crown Hopper app icon" style="background:linear-gradient(135deg,#d8892a,#3a6ac0)"></div><div class="name">Crown Hopper</div></div>
  <div class="app" style="left:456px;top:871px"><div class="price">FREE</div><div class="icon" role="img" aria-label="Tonegrid app icon" style="background:linear-gradient(#5a5a5a,#2a2a2a)"></div><div class="name">Tonegrid</div></div>
  <div class="app" style="left:579px;top:871px"><div class="price">FREE</div><div class="icon" role="img" aria-label="Kit Bench app icon" style="background:radial-gradient(#4a7ab8,#1a1e28)"></div><div class="name">Kit Bench</div></div>
  <div class="app" style="left:703px;top:871px"><div class="price">FREE</div><div class="icon" role="img" aria-label="Moonveil app icon" style="background:linear-gradient(135deg,#6a2a8a,#d24a5a)"></div><div class="name">Moonveil</div></div>
  <div class="app" style="left:826px;top:871px"><div class="price">$0.99</div><div class="icon" role="img" aria-label="Orbit Pop app icon" style="background:radial-gradient(#3aa0e8,#f08a1a)"></div><div class="name">Orbit Pop</div></div>
  <div class="app" style="left:949px;top:871px"><div class="price">FREE</div><div class="icon" role="img" aria-label="Lancer's app icon" style="background:linear-gradient(135deg,#cfd8e0,#c02a2a)"></div><div class="name">Lancer's</div></div>

  <div class="app" style="left:204px;top:1004px"><div class="price">FREE</div><div class="icon" role="img" aria-label="Zombies app icon" style="background:radial-gradient(#9ccf5a,#1d2a1a)"></div><div class="name">Zombies</div></div>
  <div class="app" style="left:333px;top:1004px"><div class="price">FREE</div><div class="icon" role="img" aria-label="Crown Hopper app icon" style="background:linear-gradient(135deg,#111,#3a3a3a)"></div><div class="name">Crown Hopper</div></div>
  <div class="app" style="left:456px;top:1004px"><div class="price">$0.99</div><div class="icon" role="img" aria-label="Tonegrid app icon" style="background:linear-gradient(#5a5a5a,#2a2a2a)"></div><div class="name">Tonegrid</div></div>
  <div class="app" style="left:579px;top:1004px"><div class="price">$0.99</div><div class="icon" role="img" aria-label="Kit Bench app icon" style="background:radial-gradient(#4a7ab8,#1a1e28)"></div><div class="name">Kit Bench</div></div>
  <div class="app" style="left:703px;top:1004px"><div class="price">FREE</div><div class="icon" role="img" aria-label="Moonveil app icon" style="background:linear-gradient(135deg,#6a2a8a,#d24a5a)"></div><div class="name">Moonveil</div></div>
  <div class="app" style="left:826px;top:1004px"><div class="price">FREE</div><div class="icon" role="img" aria-label="Orbit Pop app icon" style="background:radial-gradient(#3aa0e8,#f08a1a)"></div><div class="name">Orbit Pop</div></div>
  <div class="app" style="left:949px;top:1004px"><div class="price">FREE</div><div class="icon" role="img" aria-label="Lancer's app icon" style="background:linear-gradient(135deg,#cfd8e0,#c02a2a)"></div><div class="name">Lancer's</div></div>
</div>

<footer class="abs footer">Copyright©2013&nbsp; BrightPickDigest. All Rights Reserved</footer>

</body>
</html>
```